Broschüre für Gleichstellungsstelle einer kommunalen Stadtverwaltung
Zielgruppe
Wir sind die Gleichstellungsstelle einer kommunalen Stadtverwaltung (Einwohner*innen ca. 74.500) und richten uns mit unserer Arbeit grundsätzlich an alle Menschen.
Wir wollen eine Broschüre zum Handlungsleitfaden für die geschlechtergerechte Sprache bei der Stadt erstellen. Dieser soll an die Beschäftigten als Unterstützung verteilt werden.
Aufgabenstellung
- Broschüre mit Wire-O-Bindung, Druckformat 14,8 cm x 14,8 cm, Endformat 15,0 x 15,0 cm
- Spiralbindung an der Kopfseite
- doppelseitiges Deckblatt und Rückseite
- 16 Seiten Inhalt, wobei lediglich die Vorderseiten Text enthalten
- Schriftart (optimal Avenir Next, alternativ Arial) und Farbschema laut Corporate Design
- Der Text ist vorgegeben, die Gestaltung ist im Rahmen des Corporate Designs frei
Es soll eine ansprechende Broschüre gestaltet werden, welche die Leser*innen zum Blättern einlädt. Das bedeutet, dass alle Seiten (Deckblatt, Inhaltsseiten und Rückseiten) bei der Gestaltung berücksichtigt werden müssen.
Am Ende soll neben den üblichen Dateien auch eine fertige Druckdatei (siehe Datenblatt) zur Verfügung gestellt werden. Dabei ist zu beachten, dass die Spiralbindung des fertigen Produkts an der Kopfseite sein soll.

```html
<!DOCTYPE html>
<html lang="de">
<head>
<meta charset="utf-8">
<title>Hilfe, Tipps und Links</title>
<link rel="stylesheet" href="https://fonts.googleapis.com/css2?family=Nunito+Sans:wght@400;600;700;800&display=swap">
<style>
  :root {
    --forest: #02524a;
    --sage: #9bb5b1;
    --sage-light: #a9c2bd;
    --paper: #ffffff;
    --frame: #c9c9c9;
  }
  * { margin: 0; padding: 0; box-sizing: border-box; }
  html, body { width: 1200px; height: 1200px; overflow: hidden; background: var(--paper); }
  body { font-family: "Nunito Sans", "Avenir Next", Arial, sans-serif; }

  .page {
    position: relative;
    width: 1200px;
    height: 1200px;
    background: var(--paper);
    border: 1px solid var(--frame);
  }

  .info-band {
    position: absolute;
    left: 0; top: 0;
    width: 100%;
    height: 614px;
    background: var(--forest);
    color: var(--paper);
    padding: 127px 0 0 81px;
  }

  .info-title {
    font-size: 33px;
    font-weight: 800;
    line-height: 40px;
    letter-spacing: 0.2px;
  }

  .info-text {
    font-size: 26px;
    font-weight: 400;
    line-height: 37px;
    width: 1050px;
  }

  .contact-mail {
    display: block;
    margin: 16px 0 14px 8px;
    font-size: 25px;
    font-weight: 700;
    color: var(--sage-light);
    line-height: 37px;
  }

  .info-text.spaced { margin-top: 37px; }

  .link-list {
    position: absolute;
    left: 294px;
    top: 677px;
    list-style: none;
  }

  .link-item {
    width: 560px;
    height: 74px;
    margin-bottom: 13px;
    background: var(--sage);
    color: var(--paper);
    font-size: 33px;
    font-weight: 700;
    line-height: 74px;
    padding-left: 42px;
  }
</style>
</head>
<body>
  <div class="page">
    <section class="info-band">
      <h2 class="info-title">HILFE, TIPPS UND LINKS</h2>
      <p class="info-text">Wenn Sie Unterstützung bei der Umsetzung der geschlechtergerechten Sprache wünschen, wenden Sie sich gerne an die Gleichstellungsstelle</p>
      <span class="contact-mail">gleichstellungsbeauftragte@haldenbrueck.de).</span>
      <p class="info-text">Gemeinsam kann sicherlich für jeden Anwendungsfall eine praktikable Lösung gefunden werden.</p>
      <p class="info-text spaced">Diese Zusammenstellung bietet Ihnen Formulierungshilfen und Emp-<br>fehlungen an, darüber hinaus finden Sie auch im Internet viele Beispiele geschlechtergerechter Formulierungen. Zum Beispiel:</p>
    </section>

    <ul class="link-list">
      <li class="link-item">www.gewandtformulieren.de</li>
      <li class="link-item">www.sprachoffen.de</li>
    </ul>
  </div>
</body>
</html>
```